Designs for a Barrister's chambers

Design stationery (including business card and letterhead) for a barrister's chambers -- similar to a law firm, using the enclosed logo. The current designs are not fit for purpose.

```html
<!DOCTYPE html>
<html lang="en">
<head>
<meta charset="utf-8">
<title>Lindqvist Chambers – Business Card</title>
<link href="https://fonts.googleapis.com/css2?family=Montserrat:wght@600;700&family=Roboto+Condensed:wght@300;400;700&display=swap" rel="stylesheet">
<style>
  :root {
    --navy: #001a35;
    --teal: #0a93b0;
    --ink-grey: #4a4a4a;
    --paper: #ffffff;
    --backdrop: #dcdcdc;
  }
  * { margin: 0; padding: 0; box-sizing: border-box; }
  html, body {
    width: 1200px; height: 1101px; overflow: hidden;
    background: var(--backdrop);
  }
  .card {
    position: absolute; left: 269px; width: 704px; height: 402px;
  }
  .card--front { top: 112px; background: var(--paper); }
  .card--back  { top: 611px; background: var(--navy); }

  .brand {
    position: absolute; display: flex; align-items: center;
    font-family: "Montserrat", sans-serif; font-weight: 700;
    letter-spacing: -0.5px; line-height: 1.05;
  }
  .brand__mark { flex: none; background: var(--teal); }
  .card--front .brand { left: 66px; top: 148px; gap: 13px; color: var(--navy); font-size: 32px; }
  .card--front .brand__mark { width: 62px; height: 62px; }
  .card--back .brand { left: 165px; top: 224px; gap: 20px; color: var(--paper); font-size: 50px; }
  .card--back .brand__mark { width: 97px; height: 97px; }

  .divider {
    position: absolute; left: 338px; top: 106px; width: 1px; height: 155px;
    background: var(--navy);
  }
  .contact { position: absolute; left: 358px; top: 96px; }
  .contact__name {
    font-family: "Montserrat", sans-serif; font-weight: 700;
    font-size: 24px; color: var(--navy); line-height: 1.1;
  }
  .contact__role {
    font-family: "Montserrat", sans-serif; font-weight: 600;
    font-size: 16px; color: var(--teal); opacity: .85; letter-spacing: .5px;
  }
  .contact__lines {
    margin-top: 13px; margin-left: 3px;
    font-family: "Roboto Condensed", sans-serif; font-weight: 300;
    font-size: 16px; color: var(--ink-grey); line-height: 20px;
  }
  .contact__address { margin-bottom: 6px; }
  .contact__lines b { font-weight: 700; color: var(--navy); }

  .web-band {
    position: absolute; left: 0; top: 346px; width: 100%; height: 24px;
    background: var(--navy); color: var(--paper);
    font-family: "Roboto Condensed", sans-serif; font-size: 15px;
    letter-spacing: 7.6px; text-align: center; line-height: 24px;
  }
</style>
</head>
<body>
  <section class="card card--front">
    <div class="brand">
      <span class="brand__mark"></span>
      <span class="brand__name">Lindqvist<br>Chambers</span>
    </div>
    <div class="divider"></div>
    <div class="contact">
      <h1 class="contact__name">Daniel Marsh</h1>
      <p class="contact__role">Barrister</p>
      <div class="contact__lines">
        <p class="contact__address">42 Harrow Lane<br>London EC1A 7QB</p>
        <p><b>T:</b> 0200 555 0101</p>
        <p><b>F:</b> 0200 555 0102</p>
        <p><b>E:</b> daniel.marsh@lindqvistchambers.com</p>
      </div>
    </div>
    <div class="web-band">www.lindqvistchambers.com</div>
  </section>

  <section class="card card--back">
    <div class="brand">
      <span class="brand__mark"></span>
      <span class="brand__name">Lindqvist<br>Chambers</span>
    </div>
  </section>
</body>
</html>
```